Letterhead/Envelope Design Project

We are a 501c3 non-profit that supports educational programs at Oskenna Ridge Meadows State Park in California. We have new logo and need letterhead. The design needs need incorporate the logo attached. It needs to contain the information in document attached called "information" attached. Please see our website ridgemeadows.org to get the feeling and colors we are looking for.

```html
<!DOCTYPE html>
<html lang="en">
<head>
<meta charset="utf-8">
<title>Oskenna Ridge Meadows Association – Letterhead</title>
<link rel="stylesheet" href="https://fonts.googleapis.com/css2?family=Lato:wght@300;400&display=swap">
<style>
  :root {
    --paper: #ffffff;
    --forest: #1f4d2b;
    --contact: #d9866c;
    --rule: #e8b9a8;
  }
  html, body {
    margin: 0;
    padding: 0;
    overflow: hidden;
    background: var(--paper);
  }
  .letterhead {
    position: relative;
    width: 848px;
    height: 1200px;
    background: var(--paper);
    overflow: hidden;
    font-family: "Lato", sans-serif;
  }
  .brand {
    position: absolute;
    left: 31px;
    top: 28px;
    width: 124px;
    display: flex;
    flex-direction: column;
    align-items: flex-start;
    gap: 10px;
  }
  .brand-mark {
    width: 44px;
    height: 44px;
    background: var(--forest);
  }
  .brand-name {
    margin: 0;
    font-weight: 400;
    font-size: 15px;
    line-height: 1.25;
    letter-spacing: 0.04em;
    text-transform: uppercase;
    color: var(--forest);
  }
  .contact-rule {
    position: absolute;
    left: 581px;
    top: 47px;
    width: 1px;
    height: 110px;
    background: var(--rule);
  }
  .contact {
    position: absolute;
    left: 596px;
    top: 32px;
    margin: 0;
    font-style: normal;
    font-weight: 300;
    font-size: 17px;
    line-height: 21.4px;
    color: var(--contact);
  }
  .contact span { display: block; }
</style>
</head>
<body>
  <main class="letterhead">
    <header>
      <div class="brand">
        <div class="brand-mark"></div>
        <p class="brand-name">Oskenna Ridge<br>Meadows<br>Association</p>
      </div>
      <div class="contact-rule"></div>
      <address class="contact">
        <span>P.O. Box 4207</span>
        <span>Elmhollow, CA 95310-4207</span>
        <span>Phone: 209.555.0142</span>
        <span>Fax: 209.555.0187</span>
        <span>info@ridgemeadows.org</span>
        <span>website: ridgemeadows.org</span>
      </address>
    </header>
  </main>
</body>
</html>
```